依頼詳細
封筒2種類(角2・長3)のデザインをお願いします。
会社のロゴは決まったものがあります。
名刺デザインを踏襲したようなデザインが希望です。
記載項目
添付する名刺同様に、名刺の表の内容を表に、裏の内容を裏にお願いします
表は4Cで結構ですが、裏は1Cでお願いします。
希望イメージ
シンプル 複雑
単色 カラフル
暗い 明るい
日常 高級
遊び心 厳粛
未来的 伝統的
女性的 男性的
希望する色
青系、ベースは白でブルー系でお願いします。
納品ファイル
• イラストレーター形式 (.ai)
補足説明
ロゴは仕様書がありますので添付します。
名刺のデザインを添付します。
■ 選んだ理由

この度はご提案・ご修正等、スムーズにご対応いただきまして誠にありがとうございます。検討したました結果、tekorunosuさんにお願いすることにいたしました。23件ご提案をいただきまして、皆さんキレイなデザインで大きな違いはなく、非常に迷いましたが、数案バリエーションでご提案いただき、レスポンスが良かった点が決めてでした。

■ 提案者全員のお礼・コメント

この度はご提案・ご修正等、スムーズにご対応いただきまして誠にありがとうございます。23件ご提案をいただきまして、皆さんキレイなデザインで大きな違いはなく、非常に迷いましたが、数案バリエーションでご提案いただき、レスポンスが良かった点が決めてでした。

```html
<!DOCTYPE html>
<html lang="ja">
<head>
<meta charset="utf-8">
<title>Nagisa Works 封筒デザイン</title>
<link rel="stylesheet" href="https://fonts.googleapis.com/css2?family=Noto+Sans+JP:wght@400;500;700&family=Open+Sans:wght@400;600;700;800&display=swap">
<style>
  :root{
    --stage:#e3e3e3;
    --paper:#ffffff;
    --edge:#9a9a9a;
    --fold:#b5b5b5;
    --brand-blue:#2b7bd0;
    --brand-blue-deep:#1f5fb3;
    --ink:#2a2a2a;
    --ink-soft:#4a4a4a;
    --mono-dark:#5a5a5a;
    --mono-mid:#8a8a8a;
    --mono-light:#e6e6e6;
  }
  html,body{margin:0;padding:0;width:1200px;height:1200px;overflow:hidden;background:var(--stage);}
  .sheet{display:block;width:1200px;height:1200px;}
  .envelope-paper{fill:var(--paper);stroke:var(--edge);stroke-width:1.2;filter:drop-shadow(2px 4px 4px rgba(0,0,0,.22));}
  .fold-line{fill:none;stroke:var(--fold);stroke-width:1.2;}
  .name-front{font-family:"Open Sans",sans-serif;font-weight:800;font-size:36px;fill:var(--brand-blue);}
  .name-back{font-family:"Open Sans",sans-serif;font-weight:800;font-size:36px;fill:var(--mono-dark);}
  .company-jp{font-family:"Noto Sans JP",sans-serif;font-weight:500;font-size:16px;fill:var(--ink);}
  .company-en{font-family:"Open Sans",sans-serif;font-weight:700;font-size:15px;fill:var(--ink);}
  .address-jp{font-family:"Noto Sans JP",sans-serif;font-size:10.5px;fill:var(--ink-soft);}
  .address-en{font-family:"Open Sans",sans-serif;font-size:9.6px;fill:var(--ink-soft);}
  .url{font-family:"Open Sans",sans-serif;font-size:11px;fill:#ffffff;}
</style>
</head>
<body>
<svg class="sheet" viewBox="0 0 1200 1200" xmlns="http://www.w3.org/2000/svg">
  <defs>
    <linearGradient id="bar-blue" x1="0" x2="1">
      <stop offset="0" stop-color="var(--brand-blue-deep)"/>
      <stop offset="1" stop-color="var(--brand-blue)"/>
    </linearGradient>
    <linearGradient id="bar-grey" x1="0" x2="1">
      <stop offset="0" stop-color="var(--mono-mid)"/>
      <stop offset="1" stop-color="var(--mono-light)"/>
    </linearGradient>
    <linearGradient id="haze" x1="0" y1="1" x2="0" y2="0">
      <stop offset="0" stop-color="#f0f0f0" stop-opacity=".9"/>
      <stop offset="1" stop-color="#ffffff" stop-opacity="0"/>
    </linearGradient>
  </defs>

  <!-- Front: long envelope -->
  <g class="envelope envelope-front">
    <path class="envelope-paper" d="M120 62 H528 L564 174 V1134 H84 V174 Z"/>
    <line class="fold-line" x1="84" y1="174" x2="564" y2="174"/>
    <rect x="130" y="900" width="360" height="150" fill="url(#haze)" role="img" aria-label="淡いブランド背景装飾"/>
    <rect x="120" y="989" width="18" height="18" fill="var(--brand-blue)"/>
    <text class="name-front" x="146" y="1008">Nagisa Works</text>
    <text class="company-jp" x="120" y="1050">株式会社ナギサワークス</text>
    <text class="address-jp" x="120" y="1070">〒105-0021 東京都港区東新橋3-4-8 ハーバービル東館 702</text>
    <rect x="114" y="1080" width="428" height="21" fill="url(#bar-blue)"/>
    <text class="url" x="126" y="1095">http://www.nagisaworks.jp</text>
  </g>

  <!-- Back: long envelope -->
  <g class="envelope envelope-back">
    <path class="envelope-paper" d="M672 60 H1062 L1116 168 V1134 H624 V168 Z"/>
    <path class="fold-line" d="M630 174 Q740 186 840 194 Q960 184 1110 168"/>
    <path class="fold-line" d="M630 1128 L654 1078 H1086 L1110 1128"/>
    <rect x="658" y="860" width="360" height="140" fill="url(#haze)" role="img" aria-label="淡いブランド背景装飾"/>
    <rect x="658" y="953" width="18" height="18" fill="var(--mono-dark)"/>
    <text class="name-back" x="684" y="972">Nagisa Works</text>
    <text class="company-en" x="658" y="1002">NAGISA WORKS INC.</text>
    <line x1="658" y1="1009" x2="900" y2="1009" stroke="var(--mono-mid)" stroke-width=".8"/>
    <text class="address-en" x="658" y="1026">Harbor Bldg East 702, 3-4-8 Higashi-Shinbashi, Minato-ku, Tokyo 105-0021, Japan</text>
    <rect x="658" y="1037" width="381" height="21" fill="url(#bar-grey)"/>
    <text class="url" x="670" y="1052">http://www.nagisaworks.jp</text>
  </g>
</svg>
</body>
</html>
```